eBook Cover_H. Vollmar-Tessen
Schnell und zuverlässoig,Änderungswünsche wurden umgehend ausgeführt. Vielen Dank für das tolle Cover zu meinem ersten Buch!
Zielgruppe
freie Roman-Autorin (Erstlingswerk)
Zielgruppe: Lesende (Erwachsene), Frauen
Charakterisierung: magisch-realistischer Familienroman, spielt im Europa der Jetzt-Zeit
Aufgabenstellung
Im ersten Schritt geht es um ein Cover für ein eBook, das aber bei Bedarf als Book on Demand gedruckt werden soll. Es wird daher später Anforderung bzgl. Dicke / Umfang des gedruckten Buches und einer Rückseite geben. Das gewählte Design soll dann dahingehend überarbeitet und finale Druckdaten zur Verfügung gestellt werden. Dies soll von vornherein berücksichtigt werden und im Preis enthalten sein.
Titel: Nebel über Glas, Funken im Moor
Autorinnenname: Henrike Vollmar-Tessen
des weiteren auf dem Cover: Roman

```html
<!DOCTYPE html>
<html lang="de">
<head>
<meta charset="utf-8">
<title>Nebel über Glas, Funken im Moor – Henrike Vollmar-Tessen</title>
<link rel="stylesheet" href="https://fonts.googleapis.com/css2?family=Open+Sans:wght@400;600&family=Oswald:wght@600;700&display=swap">
<style>
  :root {
    --paper: #ffffff;
    --ink: #56606a;
    --ink-dark: #454c54;
    --red-light: #e8341a;
    --red-mid: #c8180b;
    --red-deep: #7e0804;
    --roman-white: #ffffff;
  }
  html, body {
    margin: 0;
    padding: 0;
    width: 948px;
    height: 1200px;
    overflow: hidden;
    background: var(--paper);
  }
  .cover {
    position: relative;
    width: 948px;
    height: 1200px;
    background: var(--paper);
    overflow: hidden;
  }
  .cover__author {
    position: absolute;
    top: 196px;
    left: 0;
    width: 100%;
    text-align: center;
    font-family: "Open Sans", sans-serif;
    font-weight: 400;
    font-size: 29px;
    letter-spacing: 1.5px;
    color: var(--ink-dark);
    margin: 0;
  }
  .cover__rule {
    position: absolute;
    top: 252px;
    left: 50%;
    width: 244px;
    height: 5px;
    margin-left: -122px;
    background: var(--ink);
  }
  .cover__title {
    position: absolute;
    top: 318px;
    left: 0;
    width: 100%;
    margin: 0;
    text-align: center;
    font-family: "Oswald", sans-serif;
    font-weight: 700;
    font-size: 86px;
    line-height: 102px;
    letter-spacing: 3px;
    color: var(--ink);
    text-transform: uppercase;
  }
  .cover__title span { display: block; }
  .cover__band {
    position: absolute;
    left: 0;
    top: 0;
    width: 948px;
    height: 1200px;
  }
  .cover__genre {
    position: absolute;
    top: 842px;
    left: 0;
    width: 100%;
    text-align: center;
    margin: 0;
    font-family: "Oswald", sans-serif;
    font-weight: 700;
    font-size: 62px;
    letter-spacing: 4px;
    color: var(--roman-white);
    transform: skewX(-10deg);
  }
</style>
</head>
<body>
  <main class="cover">
    <p class="cover__author">HENRIKE VOLLMAR-TESSEN</p>
    <div class="cover__rule"></div>
    <h1 class="cover__title">
      <span>Nebel über Glas</span>
      <span>Funken im Moor</span>
    </h1>

    <svg class="cover__band" viewBox="0 0 948 1200" role="img" aria-label="Rote Fläche mit geschwungenen Linien und Kreisornamenten">
      <defs>
        <linearGradient id="band-red" x1="0" y1="0" x2="0.35" y2="1">
          <stop offset="0" stop-color="var(--red-deep)"/>
          <stop offset="0.3" stop-color="var(--red-mid)"/>
          <stop offset="0.6" stop-color="var(--red-light)"/>
          <stop offset="1" stop-color="var(--red-deep)"/>
        </linearGradient>
      </defs>
      <polygon points="0,745 500,738 948,585 948,1200 0,1200" fill="url(#band-red)"/>
    </svg>

    <p class="cover__genre">ROMAN</p>
  </main>
</body>
</html>
```